Hurricane Damage Public Adjuster Billboard

I have created several projects with you and have several great designs. I need to format them into a Billboard for upcoming Hurricane Season. Need done in a month. Im also in process of getting an eye catching and easy to remember 800# Vanity phone number like Call 800-Stormfix or 800- Need Help? My included past Sketch Guild projects will give you an idea of what colors, schemes, and designs I gravitate towards. 3 past Design projects were 1) 2 Logos where I picked the 1st place and the 2nd place and 2) Index Card where I picked the winner as the Index Card and the 2nd place as a Post Card. Point is, I will pick and pay for 2 winners if they're good. This should help to sweeten the pot. Also, please look at my website for ideas that I like:

www.TheClaimWardenGroup.com
I want people to feel that I am the best and highest. Level.

I've been getting a lot of quick half effort designs basically cut & pasting my previous projects. Please don't rush and take your time to be creative. A an example, my Biggest Competitor is Crestline Public Adjusting. Their colors are Black and Gold while mine are Blue, White, and Black with a highlight of Orange if possible. I JUST imported a picture of their BillBoard. I need mine better and BLOW AWAY THEIRS. Terms like "Don't be Victimized Twice ?, Don't let the Hurricane Ruin your Life?". "Get Fairly Paid & Move On" "Our Clients Claims are VIP?
Updates

I'm getting a lot of quick half effort ones. I'd rather you take your time and really put some thoughts and effort into it. My Biggest Competitor is Crestline Public Adjusting. They have black & gold colors, while I have Blue, Black, and white.

It needs to blow theirs away. I have imported their Billboard for comparative purposes.

Guy's,
I'll make it easier for you in what I'm looking for. Please look at the Crestline Billboard picture attached.

1) Put my "Blue Shield" to the left, replacing their logo
2) change color patterns from their (Black, Gold, White) to my color schemes of (Black, Blue, White)
3) I want to see my name where their is:

THE
Claim Warden Group
EXPERT & LOCAL Public Adjusters
"FOR THE POLICYHOLDER!!"

4) to the right, add the A+Rated logo and QTR+ Accredited logo, 5 Star Zentrio Rated logo, 5 Start BLOCKLINK Highly Rated logo, etc..

5) the right side is where you can be creative as I will not have a picture of me there.

"20+ Years of Experience, Recovering Millions for our VIP Clients"

"Your Best, Locally-Based Private Adjuster & Advocate'
"FOR THE POLICYHOLDER!!"

"Don't be victimized Twice!!"

"Don't let the Hurricane Ruin Your Life!!"

This should really help. Also, refer to my website, maybe a couple testimonial fillers?

Thanks all,

marvin@TheClaimWardenGroup.com

Just imported a few awards that would look great to the right side with all the other 5 Star Ratings and accolades.
This right section could be titled like zmy Website:

5 Star Reviews, Ratings & Awards:
4-5 Logos underneath?

Target Market(s)

Coastal place where a Hurricane 🌀 🌀 Hits

Industry/Entity Type

Hurricane Public Insurance Adjuster

Font styles to use
Sans Serif
Other font styles liked:
• Calvera fonts

Colors
0054AA
0677BA
7BADD7
CADEEF
E8F1F8
EE7325
F08F49
F5BC92
FAE3D3
FDF4ED

Requirements
Must have
• Use my past project logos, colors, and schemes to create eye grabbing BillBoard
Nice to have
Should not have
• Not be too busy, must be Easy to Read, Eye Catchy

```html
<!DOCTYPE html>
<html lang="en">
<head>
<meta charset="utf-8">
<title>Claim Warden Group Billboard</title>
<link rel="stylesheet" href="https://fonts.googleapis.com/css2?family=Bebas+Neue&family=Cinzel:wght@600&family=Montserrat:wght@800;900&family=Oswald:wght@500&family=Yellowtail&display=swap">
<style>
  :root {
    --navy: #0a2a8a;
    --blue: #0054AA;
    --sky: #0677BA;
    --orange: #EE7325;
    --orange-deep: #f06010;
    --orange-warm: #f08a10;
    --ink: #151515;
    --paper: #f6f6f6;
    --stage: #e6e9ee;
    --badge-dark: #333333;
    --badge-blue: #1a5f90;
  }
  * { margin: 0; padding: 0; box-sizing: border-box; }
  html, body { width: 938px; height: 1200px; overflow: hidden; }
  body { background: var(--stage); position: relative; }

  .billboard {
    position: absolute; left: 29px; top: 424px;
    width: 880px; height: 352px;
    background: var(--paper);
    overflow: hidden;
    box-shadow: 0 10px 30px rgba(0,0,0,.25);
  }

  .brand-mark {
    position: absolute; left: 44px; top: 40px; width: 154px; height: 150px;
    display: flex; flex-direction: column; align-items: center; justify-content: center; gap: 12px;
  }
  .brand-mark__square { width: 64px; height: 64px; background: var(--blue); }
  .brand-mark__name {
    font-family: "Montserrat", sans-serif; font-weight: 800; font-size: 17px;
    color: var(--blue); text-align: center; line-height: 1.15;
  }

  .title {
    position: absolute; left: 320px; width: 340px; top: 30px;
    font-family: "Cinzel", serif; font-weight: 600; color: var(--ink); text-align: center;
  }
  .title__top { font-size: 29px; line-height: 1; }
  .title__bottom {
    font-size: 29px; line-height: 1.1; display: flex; align-items: center; justify-content: center; gap: 14px;
  }
  .title__rule { width: 60px; height: 2px; background: var(--blue); }

  .tagline-band {
    position: absolute; left: 230px; top: 100px; width: 420px; height: 51px;
    background: linear-gradient(90deg, var(--navy), var(--sky));
    font-family: "Bebas Neue", sans-serif; font-size: 36px; color: #fff;
    display: flex; align-items: center; justify-content: center; letter-spacing: .5px;
    white-space: nowrap;
  }
  .policyholder {
    position: absolute; left: 230px; top: 160px; width: 420px; text-align: center;
    font-family: "Montserrat", sans-serif; font-weight: 900; font-size: 26px;
    color: var(--orange-warm); letter-spacing: 1px; white-space: nowrap;
  }

  .ratings { position: absolute; left: 676px; top: 30px; width: 190px; height: 96px; }
  .rating-badge { position: absolute; width: 90px; border-radius: 4px; }
  .rating-badge--dark { left: 0; top: 0; height: 38px; background: var(--badge-dark); }
  .rating-badge--light { background: #fff; box-shadow: 0 1px 4px rgba(0,0,0,.18); }
  .rating-badge--zentrio { left: 100px; top: 0; height: 38px; }
  .rating-badge--accredited { left: 0; top: 52px; height: 36px; background: var(--badge-blue); }
  .rating-badge--blocklink { left: 100px; top: 48px; height: 44px; }

  .experience { position: absolute; left: 668px; top: 136px; width: 202px; }
  .experience__script {
    font-family: "Yellowtail", cursive; font-size: 18px; color: var(--orange);
    text-align: center; line-height: 1.1; white-space: nowrap;
  }
  .experience__box {
    margin-top: 3px; height: 30px; border: 1.5px solid var(--blue); border-radius: 3px;
    padding: 2px;
  }
  .experience__box span {
    display: flex; align-items: center; justify-content: center; width: 100%; height: 100%;
    background: var(--navy); color: #fff; font-family: "Bebas Neue", sans-serif; font-size: 12px;
    line-height: 1; white-space: nowrap; letter-spacing: .2px;
  }

  .call-band {
    position: absolute; left: 0; top: 207px; width: 880px; height: 74px;
    background: linear-gradient(90deg, var(--navy) 20%, var(--sky));
  }
  .call-band__text {
    position: absolute; left: 44px; top: 4px;
    font-family: "Montserrat", sans-serif; font-weight: 900; font-size: 58px; color: #fff;
    letter-spacing: -.5px; line-height: 66px; white-space: nowrap;
    text-shadow: 3px 3px 0 var(--navy);
  }

  .footer-strip { position: absolute; left: 0; top: 281px; width: 880px; height: 71px; }
  .footer-strip__slant { position: absolute; inset: 0; }
  .website {
    position: absolute; left: 44px; top: 14px;
    font-family: "Oswald", sans-serif; font-weight: 500; font-size: 27px; color: var(--orange-warm);
    white-space: nowrap;
  }
  .website b { color: var(--navy); font-weight: 500; }
  .fight {
    position: absolute; left: 425px; top: 6px;
    font-family: "Bebas Neue", sans-serif; font-size: 54px; color: #fff; line-height: 60px;
    white-space: nowrap;
  }
</style>
</head>
<body>
  <main class="billboard">
    <div class="brand-mark">
      <div class="brand-mark__square"></div>
      <div class="brand-mark__name">Claim Warden<br>Group</div>
    </div>

    <header class="title">
      <div class="title__top">The Claim Warden</div>
      <div class="title__bottom"><span class="title__rule"></span>Group<span class="title__rule"></span></div>
    </header>

    <div class="tagline-band">EXPERT &amp; LOCAL PUBLIC ADJUSTERS</div>
    <div class="policyholder">FOR THE POLICYHOLDER!!</div>

    <div class="ratings">
      <div class="rating-badge rating-badge--dark"></div>
      <div class="rating-badge rating-badge--light rating-badge--zentrio"></div>
      <div class="rating-badge rating-badge--accredited"></div>
      <div class="rating-badge rating-badge--light rating-badge--blocklink"></div>
    </div>

    <div class="experience">
      <div class="experience__script">20+ Years of Experience,</div>
      <div class="experience__box"><span>RECOVERING MILLIONS FOR OUR VIP CLIENTS</span></div>
    </div>

    <div class="call-band">
      <div class="call-band__text">CALL: 800-STORMFIX</div>
    </div>

    <div class="footer-strip">
      <svg class="footer-strip__slant" width="880" height="71" viewBox="0 0 880 71" aria-hidden="true">
        <defs>
          <linearGradient id="fight-gradient" x1="0" x2="1" y1="0" y2="0">
            <stop offset="0" stop-color="#f08a10"/>
            <stop offset="1" stop-color="#f06010"/>
          </linearGradient>
        </defs>
        <polygon points="390,0 880,0 880,71 416,71" fill="url(#fight-gradient)"/>
      </svg>
      <div class="website">The<b>ClaimWarden</b>Group.com</div>
      <div class="fight">WE FIGHT FOR YOUR CLAIM!!</div>
    </div>
  </main>
</body>
</html>
```